Business Card Design for Marketing Firm

Looking for business card design for higher end marketing firm. Clean but impressionable/trendy. We are a marketing firm that represents manufacturers in the foodservice equipment and supply industry. Our customers are end users such has hotels, restaurants, country clubs, convention centers and casinos as well as distributors of restaurants supplies and equipment, and manufacturers of foodservice equipment and supplies.
Target Market(s)
Hotels, Restaurants, Supply & Equipment Distributors, Foodservice Manufacturers
Industry/Entity Type
Foodservice/Hospitality
Contact Information for Business Card
Name, Title, Contact Number, Email, Website, Social Media, Address
Requirements
Must have
- Clean & Simple but Serious and Impressionable

```html
<!DOCTYPE html>
<html lang="en">
<head>
<meta charset="utf-8">
<title>Meridian Service Reps – Business Card</title>
<link href="https://fonts.googleapis.com/css2?family=Source+Sans+3:wght@400;600;700&display=swap" rel="stylesheet">
<style>
  :root {
    --navy: #272868;
    --paper: #ffffff;
    --backdrop: #ececec;
    --ink: #1c1c2a;
  }
  * { margin: 0; padding: 0; box-sizing: border-box; }
  html, body {
    width: 864px; height: 1200px; overflow: hidden;
    background: var(--backdrop);
    font-family: "Source Sans 3", Arial, sans-serif;
  }
  .sheet {
    position: relative; width: 864px; height: 1200px;
  }
  .card {
    position: absolute; left: 112px;
    width: 640px; height: 366px;
    background: var(--paper);
    box-shadow: 0 10px 24px rgba(0,0,0,0.18);
    overflow: hidden;
  }
  .card--front { top: 160px; }
  .card--back { top: 654px; }
  .card-shapes { position: absolute; inset: 0; }

  .brand-front {
    position: absolute; left: 0; top: 0; width: 323px; height: 366px;
    display: flex; align-items: center; justify-content: center; gap: 10px;
    color: var(--paper);
  }
  .brand-dot {
    width: 12px; height: 12px; border-radius: 50%; background: var(--paper);
  }
  .brand-name {
    font-weight: 600; font-size: 21px; letter-spacing: 1.5px; text-transform: uppercase;
  }

  .holder-name {
    position: absolute; left: 383px; top: 46px;
    font-weight: 700; font-size: 30px; color: var(--navy); letter-spacing: 0.3px;
  }
  .contact-list { position: absolute; left: 383px; top: 146px; list-style: none; }
  .contact-list li {
    height: 41.5px; font-size: 18px; color: var(--ink); line-height: 24px;
  }
  .contact-list strong { font-weight: 600; }

  .brand-back {
    position: absolute; left: 0; right: 0; top: 148px;
    display: flex; align-items: center; justify-content: center; gap: 12px;
    color: var(--navy);
  }
  .brand-back .brand-dot { background: var(--navy); width: 14px; height: 14px; }
  .brand-back .brand-name { font-size: 30px; letter-spacing: 2px; }
  .back-web {
    position: absolute; left: 198px; width: 244px; top: 292px;
    text-align: center; color: var(--paper); font-size: 17px;
  }
</style>
</head>
<body>
<main class="sheet">

  <section class="card card--front" aria-label="Business card front">
    <svg class="card-shapes" width="640" height="366" viewBox="0 0 640 366">
      <path fill="var(--navy)" d="M0 0H323V100Q323 112 335 112H353Q365 112 365 124V300Q365 312 353 312H335Q323 312 323 324V366H0Z"/>
      <path fill="var(--navy)" d="M460 0H640V9H460Q453 9 453 4.5Q453 0 460 0Z"/>
      <path fill="var(--navy)" d="M460 357H640V366H453Q453 357 460 357Z"/>
      <g fill="none" stroke="var(--paper)" stroke-width="1.8">
        <circle cx="345" cy="158" r="8"/>
        <ellipse cx="345" cy="158" rx="3.5" ry="8"/>
        <line x1="337" y1="158" x2="353" y2="158"/>
      </g>
      <g fill="var(--paper)">
        <rect x="337" y="194" width="16" height="12" rx="1.5"/>
        <path d="M338 195L345 201L352 195" fill="none" stroke="var(--navy)" stroke-width="1.6"/>
        <path d="M345 251C345 251 351 244 351 239A6 6 0 0 0 339 239C339 244 345 251 345 251Z"/>
        <circle cx="345" cy="239" r="2.3" fill="var(--navy)"/>
        <path d="M339 277C339 276 341 274 342 275L344 278C344 279 343 280 342 281C343 284 346 287 349 288C350 287 351 286 352 286L355 288C356 289 354 291 353 291C346 291 339 284 339 277Z"/>
      </g>
    </svg>
    <div class="brand-front">
      <span class="brand-dot"></span>
      <span class="brand-name">Meridian Service Reps</span>
    </div>
    <h1 class="holder-name">YOUR NAME</h1>
    <ul class="contact-list">
      <li>www.dummytext.com</li>
      <li>dummytext@gmail.com</li>
      <li>Address_<strong>dummytext</strong></li>
      <li>000-000-000</li>
    </ul>
  </section>

  <section class="card card--back" aria-label="Business card back">
    <svg class="card-shapes" width="640" height="366" viewBox="0 0 640 366">
      <path fill="var(--navy)" d="M0 326H186Q198 326 198 314V291Q198 279 210 279H430Q442 279 442 291V314Q442 326 454 326H640V366H0Z"/>
    </svg>
    <div class="brand-back">
      <span class="brand-dot"></span>
      <span class="brand-name">Meridian Service Reps</span>
    </div>
    <p class="back-web">www.dummytext.com</p>
  </section>

</main>
</body>
</html>
```